Fence Flyer to Attract More Sales During Winter

We need a new flyer made that we can distribute to residential mailboxes. The flyer is to promote our Frostline Picket Days. We like simply designs, and we would like the flyer to showcase a lot of our fence photos. More of our photos are online at our website at www.getbramblerail.com - our new address needs to also be featured on the flyer - 436 Quillen rd, Monroe, NC 28117. I do want the words "FROSTLINE PICKET DAYS" to be dominate on the flyer with the description "Wood fences starting at $12/FT!" Please look through our Facebook page and our website to gather more photos or information. We are flexible on colors, nothing to fancy - simple flyer design please.

Target Market(s)

Residential homeowners that need a new fence to enclose their yard for safety, security or decorative

Industry/Entity Type

Residential Construction

Font styles to use
Sans Serif

Colors

Designer to choose colors to be used in the design.

Requirements
Must have
• Frostline Picket Days
• Contact information for the business
• "Come visit our outdoor showroom, open 24/7!"
Nice to have
• Photos of our fences - you can find more on our website at www.GetBrambleRail.com or Facebook.com/MeadowlarkRailGPV
Should not have
• Flashy designs

```html
<!DOCTYPE html>
<html lang="en">
<head>
<meta charset="utf-8">
<title>Bramble Rail Fence – Frostline Picket Days Flyer</title>
<link rel="stylesheet" href="https://fonts.googleapis.com/css2?family=Oswald:wght@600;700&family=Lato:ital,wght@0,400;0,700;0,900;1,700&display=swap">
<style>
  :root {
    --page-bg: #dfeaf6;
    --flyer-top: #c9d9ea;
    --flyer-bottom: #dbe6f1;
    --brand-blue: #3f86d3;
    --headline-blue: #3d7fcb;
    --sky-blue: #8ab9e8;
    --orange: #ec8d2c;
    --brown: #5a3a24;
    --ink: #3a3a3a;
    --white: #ffffff;
  }
  * { box-sizing: border-box; margin: 0; padding: 0; }
  html, body { width: 1200px; height: 1200px; overflow: hidden; }
  body { background: var(--page-bg); font-family: "Lato", sans-serif; color: var(--ink); }

  .flyer {
    position: absolute; left: 160px; top: 30px; width: 880px; height: 1140px;
    background: linear-gradient(180deg, var(--flyer-top), var(--flyer-bottom));
    box-shadow: 0 12px 30px rgba(40, 70, 110, 0.25);
    overflow: hidden;
  }
  .abs { position: absolute; }

  .header-swoosh { left: 0; top: 0; }
  .brand { left: 30px; top: 36px; display: flex; align-items: flex-start; gap: 12px; }
  .brand-dot { width: 22px; height: 22px; border-radius: 50%; background: var(--orange); margin-top: 4px; }
  .brand-name { font-weight: 900; font-size: 22px; color: var(--brand-blue); line-height: 1.1; }
  .brand-phone { font-weight: 900; font-size: 20px; color: #222; margin-top: 2px; }
  .brand-tagline { font-size: 8px; font-weight: 700; color: #333; margin-top: 4px; }

  .headline { left: 355px; top: 18px; font-family: "Oswald", sans-serif; font-weight: 700; color: var(--headline-blue); line-height: 1; text-shadow: 2px 2px 0 var(--white); }
  .headline-top { display: block; font-size: 104px; letter-spacing: 0.5px; }
  .headline-bottom { display: block; font-size: 70px; margin-top: 4px; }

  .offer-band { left: 200px; top: 226px; width: 520px; height: 46px; background: linear-gradient(90deg, rgba(255,255,255,0), rgba(255,255,255,0.75) 35%); }
  .offer-text { right: 178px; top: 234px; font-style: italic; font-weight: 700; font-size: 26px; color: #4a3626; }
  .price-badge {
    left: 708px; top: 161px; width: 144px; height: 144px; border-radius: 50%;
    background: var(--orange); border: 6px solid var(--white);
    box-shadow: 0 4px 10px rgba(0,0,0,0.2);
    display: flex; align-items: center; justify-content: center;
    font-family: "Oswald", sans-serif; font-weight: 600; font-size: 40px; color: var(--white);
  }

  .intro { left: 30px; top: 316px; width: 800px; font-size: 18px; line-height: 23px; color: #333; }
  .intro strong { font-weight: 900; }

  .photo { border: 4px solid var(--white); box-shadow: 0 1px 4px rgba(0,0,0,0.2); }
  .photo-wood { background: linear-gradient(160deg, #5f7d3f 0%, #b79a6a 45%, #d7c197 70%, #7c6444 100%); }
  .photo-yard { background: linear-gradient(170deg, #3e6a2e 0%, #c5ad80 50%, #e0cfa6 75%, #6e5a3e 100%); }
  .photo-sky  { background: linear-gradient(180deg, #8db3db 0%, #cdb891 45%, #dcc9a0 75%, #85704a 100%); }

  .perks { left: 292px; top: 842px; list-style: none; }
  .perks li { display: flex; align-items: center; gap: 8px; font-weight: 900; font-size: 16px; color: var(--brand-blue); height: 23px; text-transform: uppercase; }

  .bottom-waves { left: 0; top: 860px; }
  .showroom { left: 24px; top: 910px; font-style: italic; font-weight: 700; font-size: 21px; line-height: 26px; color: var(--white); }

  .contact { left: 236px; top: 1000px; }
  .contact-name { font-weight: 700; font-size: 22px; color: var(--brand-blue); margin-left: 24px; margin-bottom: 2px; }
  .contact-line { display: flex; align-items: center; gap: 8px; font-size: 19px; color: #2f2f2f; height: 23px; }
  .contact-line svg { flex: none; }

  .social { top: 1071px; width: 44px; height: 44px; border-radius: 50%; background: var(--orange); }
  .social-one { left: 82px; }
  .social-two { left: 136px; }

  .brand-mark { left: 620px; top: 800px; width: 250px; height: 300px; }
  .brand-mark-sun { left: 12px; top: 6px; width: 66px; height: 66px; border-radius: 50%; background: var(--orange); }
  .brand-mark-name { left: 10px; top: 110px; font-weight: 900; font-size: 58px; line-height: 1; color: var(--brown); }
</style>
</head>
<body>
<main class="flyer">
  <svg class="abs header-swoosh" width="360" height="200" viewBox="0 0 360 200" aria-hidden="true">
    <path d="M0,0 H345 C330,90 230,170 100,168 C55,167 20,150 0,130 Z" fill="var(--white)"/>
    <path d="M0,130 C40,170 110,190 200,180 C150,196 60,196 0,165 Z" fill="var(--orange)"/>
    <path d="M345,0 H358 C342,110 230,185 110,178 C230,170 330,100 345,0 Z" fill="var(--brand-blue)"/>
  </svg>

  <div class="abs brand">
    <span class="brand-dot"></span>
    <div>
      <div class="brand-name">Bramble Rail Fence</div>
      <div class="brand-phone">704-555-0142</div>
      <div class="brand-tagline">"Because Good Fences Make Good Neighbors"</div>
    </div>
  </div>

  <h1 class="abs headline">
    <span class="headline-top">FROSTLINE</span>
    <span class="headline-bottom">PICKET DAYS!</span>
  </h1>

  <div class="abs offer-band"></div>
  <p class="abs offer-text">Wooden Fence Starting at</p>
  <div class="abs price-badge">$12/FT</div>

  <p class="abs intro">We are growing team of individuals with over <strong>30 years of experience</strong> within the fencing industry. Each member of our staff is well-trained and knowledgable within their own specialty. All of our installers take pride in the work completed. In our eyes, we are only as successful as the completion of your job. Each job is important to us and we strive to give you the best installation experience possible.</p>

  <div class="abs photo photo-yard" style="left:26px;top:454px;width:156px;height:205px" role="img" aria-label="Photo of a split rail fence with an arched wooden gate"></div>
  <div class="abs photo photo-wood" style="left:194px;top:454px;width:154px;height:205px" role="img" aria-label="Photo of a tall wooden privacy fence beside garden shrubs"></div>
  <div class="abs photo photo-wood" style="left:360px;top:454px;width:156px;height:205px" role="img" aria-label="Photo of a long wooden privacy fence along a wooded yard"></div>
  <div class="abs photo photo-sky" style="left:528px;top:454px;width:154px;height:205px" role="img" aria-label="Photo of a scalloped wooden fence beside a house"></div>
  <div class="abs photo photo-sky" style="left:694px;top:454px;width:154px;height:205px" role="img" aria-label="Photo of a tall wooden gate in a privacy fence"></div>
  <div class="abs photo photo-yard" style="left:148px;top:672px;width:201px;height:152px" role="img" aria-label="Photo of a wooden fence section with a rail fence around a lawn"></div>
  <div class="abs photo photo-sky" style="left:361px;top:672px;width:204px;height:152px" role="img" aria-label="Photo of a new shadowbox wooden fence in front of a brick home"></div>

  <ul class="abs perks">
    <li><svg width="22" height="20" viewBox="0 0 22 20" aria-hidden="true"><circle cx="9" cy="11" r="7.5" fill="none" stroke="var(--orange)" stroke-width="2"/><path d="M5 11 L9 15 L20 2" fill="none" stroke="var(--orange)" stroke-width="2.5"/></svg>Free Estimates</li>
    <li><svg width="22" height="20" viewBox="0 0 22 20" aria-hidden="true"><circle cx="9" cy="11" r="7.5" fill="none" stroke="var(--orange)" stroke-width="2"/><path d="M5 11 L9 15 L20 2" fill="none" stroke="var(--orange)" stroke-width="2.5"/></svg>HOA Approval Assistance</li>
    <li><svg width="22" height="20" viewBox="0 0 22 20" aria-hidden="true"><circle cx="9" cy="11" r="7.5" fill="none" stroke="var(--orange)" stroke-width="2"/><path d="M5 11 L9 15 L20 2" fill="none" stroke="var(--orange)" stroke-width="2.5"/></svg>Outstanding Warranty</li>
  </ul>

  <svg class="abs bottom-waves" width="880" height="280" viewBox="0 0 880 280" aria-hidden="true">
    <path d="M0,28 C120,10 260,30 420,90 C500,120 560,130 620,140 L0,280 Z" fill="var(--sky-blue)"/>
    <path d="M0,205 C140,130 320,100 520,105 C640,108 760,150 880,210 V280 H0 Z" fill="var(--white)"/>
  </svg>

  <p class="abs showroom">Come Visit Our<br>Outdoor Showroom!<br>Open 24/7</p>

  <address class="abs contact" style="font-style:normal">
    <div class="contact-name">Bramble Rail Fence</div>
    <div class="contact-line"><svg width="16" height="16" viewBox="0 0 16 16" aria-hidden="true"><path d="M3 2 L6 2 L7 5 L5 6.5 C6 9 7.5 10.5 10 11.5 L11.5 9.5 L14.5 10.5 L14.5 13.5 C8 14 2.5 8.5 3 2 Z" fill="none" stroke="var(--brand-blue)" stroke-width="1.5"/></svg>704-555-0142</div>
    <div class="contact-line"><svg width="16" height="18" viewBox="0 0 16 18" aria-hidden="true"><path d="M8 17 C3 11 2 8.5 2 6.5 A6 6 0 0 1 14 6.5 C14 8.5 13 11 8 17 Z" fill="var(--brand-blue)"/><circle cx="8" cy="6.5" r="2.2" fill="var(--white)"/></svg>436 Quillen rd, Monroe, NC 28117</div>
    <div class="contact-line"><svg width="16" height="14" viewBox="0 0 16 14" aria-hidden="true"><rect x="1" y="2" width="14" height="10" fill="none" stroke="var(--brand-blue)" stroke-width="1.5"/><path d="M1 2 L8 8 L15 2" fill="none" stroke="var(--brand-blue)" stroke-width="1.5"/></svg>office@getbramblerail.com</div>
    <div class="contact-line"><svg width="16" height="16" viewBox="0 0 16 16" aria-hidden="true"><circle cx="8" cy="8" r="6.5" fill="none" stroke="var(--brand-blue)" stroke-width="1.5"/><path d="M1.5 8 H14.5 M8 1.5 C5 5 5 11 8 14.5 M8 1.5 C11 5 11 11 8 14.5" fill="none" stroke="var(--brand-blue)" stroke-width="1.2"/></svg>www.getbramblerail.com</div>
  </address>

  <span class="abs social social-one" role="img" aria-label="Social page link"></span>
  <span class="abs social social-two" role="img" aria-label="Social page link"></span>

  <div class="abs brand-mark">
    <span class="abs brand-mark-sun"></span>
    <p class="abs brand-mark-name">Bramble<br>Rail</p>
  </div>
</main>
</body>
</html>
```